Speisekarten für ein Seerestaurant/Pizzeria
Zielgruppe
Wir sin ein Seerestaurant/Pizzeria in einem Ferien Ort
Aufgabenstellung
Wir brauchen Speisekarte in A4 und A5 Format und wichtig dass wir das Inhalt immer einfach bearbeiten können

```html
<!DOCTYPE html>
<html lang="de">
<head>
<meta charset="utf-8">
<title>Möwli Seerestaurant – Speisekarte</title>
<link rel="stylesheet" href="https://fonts.googleapis.com/css2?family=Oswald:wght@300;400;500&family=Open+Sans:ital,wght@0,400;0,600;1,400&family=Great+Vibes&display=swap">
<style>
:root{
  --canvas:#dadbdc;
  --paper:#ffffff;
  --ink:#2a2a2a;
  --muted:#5a5a5a;
  --red:#b3261e;
  --leader:#9a9a9a;
}
*{margin:0;padding:0;box-sizing:border-box}
html,body{width:1200px;height:2400px;overflow:hidden;background:var(--canvas)}
body{position:relative;font-family:"Open Sans",Arial,sans-serif;color:var(--ink)}

/* ---------- Cover ---------- */
.cover{position:absolute;left:589px;top:47px;width:358px;height:505px;overflow:hidden;
  box-shadow:0 2px 8px rgba(0,0,0,.18);
  background:linear-gradient(180deg,#7fa6d6 0%,#9dbde3 35%,#5b87b0 55%,#2f5f86 68%,#7d5a40 82%,#5a3b27 100%)}
.cover-welcome{position:absolute;top:22px;left:0;right:0;text-align:center;
  font-family:"Great Vibes",cursive;font-size:32px;color:#fff}
.cover-panel{position:absolute;left:51px;top:75px;width:255px;height:357px;background:rgba(255,255,255,.92)}
.cover-map{position:absolute;left:40px;top:8px;width:190px;height:200px;border-radius:45% 55% 40% 60%;
  background:radial-gradient(ellipse at 50% 45%,#d3e6f5 0%,#e4f0f9 55%,rgba(255,255,255,0) 75%)}
.cover-bird{position:absolute;left:87px;top:60px;width:90px;height:108px;border-radius:6px;
  background:linear-gradient(180deg,#c9cdd1 0%,#9ea3a8 60%,#7b7f83 100%)}
.cover-name{position:absolute;left:0;right:0;top:168px;text-align:center;
  font-family:"Oswald",sans-serif;font-weight:500;font-size:44px;color:#2d2d2d;letter-spacing:-.5px}
.cover-sub{position:absolute;left:0;right:0;text-align:center;font-family:"Oswald",sans-serif;font-weight:300;color:#2d2d2d}
.cover-sub.l1{top:240px;font-size:16px;letter-spacing:4px}
.cover-sub.l2{top:264px;font-size:16px;letter-spacing:3.5px}
.cover-address{position:absolute;left:0;right:0;top:325px;text-align:center;font-size:6.4px;letter-spacing:1px;line-height:1.75;color:#333}

/* ---------- Spreads ---------- */
.spread{position:absolute;left:232px;width:715px;height:505px;display:flex;box-shadow:0 2px 10px rgba(0,0,0,.2)}
.spread-1{top:616px}.spread-2{top:1191px}.spread-3{top:1784px}
.page{position:relative;width:357.5px;height:505px;overflow:hidden}
.page-bg{position:absolute;inset:0}
.bg-lake{background:linear-gradient(160deg,#0e3a6a 0%,#2d6fa8 40%,#4a8cc4 70%,#1e4d7c 100%)}
.bg-pizza{background:linear-gradient(170deg,#6b2e18 0%,#a5502a 35%,#3d4e24 60%,#7a3520 100%)}
.bg-shore{background:linear-gradient(180deg,#3e8aa7 0%,#8fb6c6 35%,#6d8c8c 60%,#34607a 100%)}
.bg-food{background:linear-gradient(180deg,#c07a3a 0%,#8c9d4a 35%,#c58a3a 60%,#6f8f3a 100%)}
.bg-lake2{background:linear-gradient(180deg,#2a5f9a 0%,#6d97bf 40%,#5e8a6f 70%,#3b6d95 100%)}
.bg-tomato{background:linear-gradient(180deg,#9c2a1c 0%,#c8553b 35%,#b7893f 65%,#843020 100%)}
.sheet{position:absolute;left:18px;right:17px;top:19px;bottom:16px;background:var(--paper);padding:16px 19px 14px}
.sheet-footer{position:absolute;left:0;right:0;bottom:6px;text-align:center;font-size:3.6px;color:#666}

/* ---------- Type ---------- */
.section-title{font-family:"Oswald",sans-serif;font-weight:400;font-size:9.5px;letter-spacing:3px;text-align:center;color:var(--ink);line-height:1.45}
.section-title.left{text-align:left}
.section-sub{font-family:"Oswald",sans-serif;font-weight:400;font-size:5.8px;letter-spacing:1.5px;text-align:center;margin-top:3px}
.section-intro{font-size:4.2px;line-height:1.5;text-align:center;color:var(--muted);margin:6px auto 0;max-width:230px}
.tagline{font-family:"Oswald",sans-serif;font-weight:300;font-size:6.2px;letter-spacing:.6px;text-align:center;color:#444;margin-top:4px}
.script-title{font-family:"Great Vibes",cursive;font-size:38px;color:var(--red);text-align:center;line-height:1;margin-top:14px}

.item{margin-top:7px}
.item-line{display:flex;align-items:baseline}
.item-name{font-family:"Oswald",sans-serif;font-weight:300;font-size:8px;letter-spacing:.4px;color:var(--ink);line-height:1.1}
.leader{flex:1;border-bottom:1px dotted var(--leader);margin:0 3px;transform:translateY(-1px);min-width:6px}
.price{font-family:"Oswald",sans-serif;font-weight:300;font-size:5.4px;letter-spacing:1px;min-width:20px;color:var(--ink)}
.item-desc{font-style:italic;font-size:4.1px;line-height:1.45;color:var(--muted);margin-top:1px;max-width:88%}

/* item with stacked prices beside name and description */
.item.split{display:flex;align-items:flex-start}
.item.split .split-main{flex:1;min-width:0}
.item.split .item-desc{max-width:100%}
.price-block{font-family:"Oswald",sans-serif;font-weight:300;font-size:5px;letter-spacing:.6px;line-height:1.15;min-width:20px;padding-top:2px}
.price-block small{display:block;font-family:"Open Sans",sans-serif;font-style:italic;font-size:3.6px;letter-spacing:0;color:var(--muted)}

.cols{display:flex;gap:16px}
.col{flex:1}
.narrow{width:200px;margin:0 auto}

.photo{border-radius:1px}
.photo-row{display:flex;gap:6px;justify-content:center}

.red-divider{display:flex;align-items:center;gap:8px;margin-top:14px;color:var(--red);
  font-family:"Oswald",sans-serif;font-weight:400;font-size:5.6px;letter-spacing:1.6px}
.red-divider::before,.red-divider::after{content:"";flex:1;border-top:.8px solid var(--red)}

.origin{font-family:"Oswald",sans-serif;font-weight:300;font-size:3.6px;letter-spacing:.4px;line-height:2.4;color:#444}
.origin b{font-weight:500;letter-spacing:.8px}
.note-red{color:var(--red);font-family:"Oswald",sans-serif;font-size:3.4px;letter-spacing:.4px;line-height:1.5}
.note{font-size:3.6px;color:#555}

.extras{display:flex;gap:22px;justify-content:center;margin-top:10px;font-family:"Oswald",sans-serif;font-weight:300;font-size:3.8px;letter-spacing:.6px;line-height:1.5}
.extras h4{color:var(--red);font-weight:400;font-size:3.8px}
</style>
</head>
<body>

<!-- Cover -->
<section class="cover">
  <div class="cover-welcome">Herzlich Willkommen</div>
  <div class="cover-panel">
    <div class="cover-map" role="img" aria-label="Zarte Seekarte im Hintergrund"></div>
    <div class="cover-bird" role="img" aria-label="Zeichnung einer Möwe auf einem Holzpfahl"></div>
    <div class="cover-name">Möwli</div>
    <div class="cover-sub l1">Seerestaurant</div>
    <div class="cover-sub l2">SEEBLICK – Seedorf</div>
    <div class="cover-address">Uferweg 12 · 6300 Seedorf<br>moewli-see.ch</div>
  </div>
</section>

<!-- Spread 1 -->
<section class="spread spread-1">
  <div class="page">
    <div class="page-bg bg-lake" role="img" aria-label="Foto Seeufer in Blautönen"></div>
    <div class="sheet">
      <p class="tagline">Feine regionale- &amp; italienische Küche</p>
      <h1 class="script-title">Wir empfehlen</h1>
      <h2 class="section-title" style="margin-top:18px">BARBECUE SPEZIALITÄTEN<br>AUS DEM SMOKER</h2>
      <p class="section-intro">Barbecue Gerichte werden 6-12 Stunden im Smoker gegart. Wir verwenden ausschliesslich Schweizer Fleisch und Bio Hickory Holz für das typische BBQ-Erlebnis und Rauch-Aroma.</p>
      <div style="padding:0 52px;margin-top:6px">
        <div class="item"><div class="item-line"><span class="item-name">BBQ SPARE RIBS</span><span class="leader"></span><span class="price">42.50</span></div>
          <p class="item-desc">aus dem Smoker mit Kirsch-Rauch Glasur<br>serviert mit Pommes frites</p></div>
        <div class="item"><div class="item-line"><span class="item-name">PULLED BEEF Burger</span><span class="leader"></span><span class="price">31.50</span></div>
          <p class="item-desc">Hausgemachte Bun, Pulled Beef (180g), BBQ-Sauce, Cheddar-Käse, Coleslaw (Kabissalat) und Jalapeno, serviert mit Pommes</p></div>
        <div class="item"><div class="item-line"><span class="item-name">PULLED PORK Burger</span><span class="leader"></span><span class="price">27.50</span></div>
          <p class="item-desc">Hausgemachte Bun, Pulled Pork (180g), BBQ-Sauce, Cheddar-Käse, Coleslaw (Kabissalat) und Jalapeno, serviert mit Pommes</p></div>
        <div class="item"><div class="item-line"><span class="item-name">PULLED VEGI Burger</span><span class="leader"></span><span class="price">25.50</span></div>
          <p class="item-desc">Hausgemachte Bun, BBQ-Sauce, Cheddar-Käse, Coleslaw (Kabissalat) und Jalapeno, serviert mit Pommes</p></div>
      </div>
      <div style="display:flex;gap:6px;margin-top:30px;align-items:flex-start">
        <div class="photo" role="img" aria-label="Foto Spare Ribs mit Pommes" style="width:91px;height:80px;background:linear-gradient(135deg,#6a3f2a,#a0644a,#3a2a22)"></div>
        <div class="photo" role="img" aria-label="Foto Pulled-Pork-Burger mit Pommes" style="width:91px;height:80px;background:linear-gradient(135deg,#c8893a,#8a4a2a,#e0b060)"></div>
        <div class="origin" style="margin-left:4px">
          <b>HERKUNFT UNSERER FRISCHPRODUKTE:</b><br>
          <b>SCHWEINEFLEISCH</b> Schweiz<br>
          <b>GEFLÜGEL</b> Schweiz<br>
          <b>RINDFLEISCH</b> Schweiz / Argentinien / Uruguay<br>
          <b>WILD</b> Schweiz / Slowenien / Ungarn<br>
          <b>FISCH</b> Schweiz / Russland / Vietnam<br>
          Produkte aus dem Ausland können Antibiotika enthalten.
        </div>
      </div>
      <p class="sheet-footer">Alle Preise verstehen sich in CHF und inkl. Mehrwertsteuer.</p>
    </div>
  </div>

  <div class="page">
    <div class="page-bg bg-pizza" role="img" aria-label="Foto Pizza und Zutaten"></div>
    <div class="sheet">
      <h2 class="section-title" style="margin-top:2px">UNSERE PIZZEN</h2>
      <p class="section-sub">NACH ORIGINAL SÜD-ITALIENISCHER REZEPTUR</p>
      <p class="section-intro">Unsere Pizza wird traditionell nach süditalienischem Rezept und mit besonders hochwertigen Zutaten zubereitet. Unser Teig ist bis zu 72 Stunden in Ruhe gereift, um Verdaulichkeit und Leichtigkeit zu gewährleisten.</p>
      <div class="cols" style="margin-top:7px">
        <div class="col">
          <div class="item"><div class="item-line"><span class="item-name">MARINARA</span><span class="leader"></span><span class="price">14.50</span></div><p class="item-desc">San Marzano Tomaten, Knoblauch, Basilikum, extra natives Olivenöl</p></div>
          <div class="item"><div class="item-line"><span class="item-name">MARGHERITA</span><span class="leader"></span><span class="price">18.00</span></div><p class="item-desc">San Marzano Tomaten, Mozzarella Fior di Latte, Basilikum, extra natives Olivenöl</p></div>
          <div class="item"><div class="item-line"><span class="item-name">PROSCIUTTO COTTO</span><span class="leader"></span><span class="price">22.00</span></div><p class="item-desc">San Marzano Tomaten, Mozzarella Fior di Latte, italienischer Hinterschinken, Oregano</p></div>
          <div class="item"><div class="item-line"><span class="item-name">PROSCIUTTO E FUNGHI</span><span class="leader"></span><span class="price">23.50</span></div><p class="item-desc">San Marzano Tomaten, Mozzarella Fior di Latte, italienischer Hinterschinken, Champignons, Oregano</p></div>
          <div class="item"><div class="item-line"><span class="item-name">NAPOLI</span><span class="leader"></span><span class="price">23.50</span></div><p class="item-desc">San Marzano Tomaten, Mozzarella Fior di Latte, Kapern, Sardellen, Taggiasche Oliven, Oregano</p></div>
          <div class="item"><div class="item-line"><span class="item-name">CALABRESE</span><span class="leader"></span><span class="price">22.00</span></div><p class="item-desc">San Marzano Tomaten, Mozzarella Fior di Latte Pikanter kalabrischer Salami, Oregano</p></div>
        </div>
        <div class="col">
          <div class="item"><div class="item-line"><span class="item-name">QUATTRO FORMAGGI</span><span class="leader"></span><span class="price">21.00</span></div><p class="item-desc">4 verschiedene Käsesorten, extra natives Olivenöl</p></div>
          <div class="item"><div class="item-line"><span class="item-name">CACCIATORE</span><span class="leader"></span><span class="price">24.00</span></div><p class="item-desc">San Marzano Tomaten, Mozzarella Fior di Latte, Speck, Knoblauch, Zwiebeln, Oregano</p></div>
          <div class="item"><div class="item-line"><span class="item-name">SPINACI E AGLIO</span><span class="leader"></span><span class="price">23.00</span></div><p class="item-desc">San Marzano Tomaten, Mozzarella Fior di Latte, Spinat, Knoblauch, Zwiebeln, Oregano</p></div>
          <div class="item"><div class="item-line"><span class="item-name">HAWAII</span><span class="leader"></span><span class="price">23.00</span></div><p class="item-desc">San Marzano Tomaten, Mozzarella Fior di Latte, Ananas, Vorderschinken, Oregano</p></div>
          <div class="item"><div class="item-line"><span class="item-name">QUATTRO STAGIONI</span><span class="leader"></span><span class="price">24.00</span></div><p class="item-desc">San Marzano Tomaten, Mozzarella Fior di Latte, Hinterschinken, Champignons, Artischocken, Taggiasche Oliven,</p></div>
          <div class="item"><div class="item-line"><span class="item-name">VEGI</span><span class="leader"></span><span class="price">22.00</span></div><p class="item-desc">San Marzano Tomaten, Mozzarella Fior di Latte, Verschiedene Gemüse Parmigiano DOP</p></div>
        </div>
      </div>
      <div class="red-divider">SPEZIAL PIZZEN FÜR ECHTE GENIESSER</div>
      <div class="cols" style="margin-top:4px">
        <div class="col">
          <div class="item"><div class="item-line"><span class="item-name">CONTADINA PIKANTE</span><span class="leader"></span><span class="price">25.00</span></div><p class="item-desc">San Marzano Tomaten, Mozzarella Fior di Latte, Hinterschinken, Champignons, pikanter kalabrischer Salami, Ei, Oregano</p></div>
          <div class="item"><div class="item-line"><span class="item-name">MÖWLI</span><span class="leader"></span><span class="price">32.00</span></div><p class="item-desc">San Marzano Tomaten, Mozzarella Fior di Latte, Burrata, 30 Monate gereifter San Daniela Rohschinken, Ruccola, Cherry-Tomaten, Balsamico e Creme extra natives Olivenöl</p></div>
          <div class="item"><div class="item-line"><span class="item-name">ORO DI SICILIA</span><span class="leader"></span><span class="price">31.50</span></div><p class="item-desc">Mozzarella Fior di Latte, Gorgonzola, Burrata, Cherry-Tomaten, Hinterschinken, Pistazien-Pesto, extra natives Olivenöl</p></div>
        </div>
        <div class="col">
          <div class="item"><div class="item-line"><span class="item-name">PRINCIPESSA</span><span class="leader"></span><span class="price">27.00</span></div><p class="item-desc">San Marzano Tomaten, Mozzarella Fior di Latte, 30 Monate gereifter San Daniela Rohschinken, Mascarpone, Oregano</p></div>
          <div class="item"><div class="item-line"><span class="item-name">SAN DANIELA</span><span class="leader"></span><span class="price">26.50</span></div><p class="item-desc">San Marzano Tomaten, Mozzarella Fior di Latte, 30 Monate gereifter San Daniela Rohschinken, Ruccola, Parmigiano DOP</p></div>
          <div class="item"><div class="item-line"><span class="item-name">PIETRO</span><span class="leader"></span><span class="price">30.50</span></div><p class="item-desc">San Marzano Tomaten, Mozzarella Fior di Latte, Zwiebeln, Knoblauch, 5 Stück Riesencrevetten, Oregano</p></div>
          <p class="note" style="margin-top:8px">Wir verwenden:</p>
          <p class="note-red">SAN MARZANO TOMATEN DOP, DEN ORIGINALEN FIOR DI LATTE MOZZARELLA<br>AUS ITALIEN UND OREGANO AUS SIZILIEN</p>
        </div>
      </div>
      <p class="sheet-footer">Alle Preise verstehen sich in CHF und inkl. Mehrwertsteuer.</p>
    </div>
  </div>
</section>

<!-- Spread 2 -->
<section class="spread spread-2">
  <div class="page">
    <div class="page-bg bg-shore" role="img" aria-label="Foto Seepromenade mit Laterne"></div>
    <div class="sheet">
      <h2 class="section-title left" style="margin-top:6px">SUPPEN</h2>
      <div style="display:flex;gap:40px;margin-top:2px">
        <div style="width:135px">
          <div class="item"><div class="item-line"><span class="item-name">TOMATENCRÈMESUPPE</span><span class="leader"></span><span class="price">10.50</span></div><p class="item-desc">mit Schlagrahm</p></div>
          <div class="item"><div class="item-line"><span class="item-name">BOUILLON</span><span class="leader"></span><span class="price">10.50</span></div><p class="item-desc">mit Tortellini</p></div>
          <div class="item split"><div class="split-main"><div class="item-line"><span class="item-name">GULASCHSUPPE</span><span class="leader"></span></div><p class="item-desc">...die Echte – nach ungarischer Art</p></div><span class="price-block">12.50<small>Vorspeise</small>19.50<small>Hauptgang</small></span></div>
        </div>
        <div class="photo" role="img" aria-label="Foto Gulaschsuppe mit Brot" style="width:91px;height:80px;margin-top:2px;background:linear-gradient(135deg,#e8d6b0,#8a3a20,#d9b98a)"></div>
      </div>
      <h2 class="section-title" style="margin-top:30px">SALATE</h2>
      <p class="section-intro" style="margin-top:2px">Alle Salate Reichen wir mit hausgemachter Salatsauce Ihrer Wahl und frischem Pizzabrot</p>
      <div class="cols" style="margin-top:14px;gap:30px">
        <div class="col">
          <div class="item"><div class="item-line"><span class="item-name">GRÜNER SALAT</span><span class="leader"></span><span class="price">10.50</span></div></div>
          <div class="item"><div class="item-line"><span class="item-name">GEMISCHTER SALAT</span><span class="leader"></span><span class="price">13.50</span></div></div>
          <div class="item"><div class="item-line"><span class="item-name">CEASAR SALAT</span><span class="leader"></span><span class="price">20.50</span></div><p class="item-desc">Eisberg Salat, Speckstreifen, Croutons &amp; Parmigiano DOP. an französische Sauce</p></div>
          <div class="item"><div class="item-line"><span class="item-name">NÜSSLISALAT</span><span class="leader"></span><span class="price">11.50</span></div><p class="item-desc">mit Speck, Brotcroûtons und Ei</p></div>
          <div class="item split"><div class="split-main"><div class="item-line"><span class="item-name">KRETA SALAT</span><span class="leader"></span></div><p class="item-desc">mit Peperoni, Gurken, Fetakäse, Oliven &amp; Tomatenwürfeln an italienischer Sauce</p></div><span class="price-block">14.50<small>Vorspeise</small>20.50<small>Hauptgang</small></span></div>
        </div>
        <div class="col">
          <div class="item split"><div class="split-main"><div class="item-line"><span class="item-name">WURST-KÄSE SALAT</span><span class="leader"></span></div></div><span class="price-block">16.50<small>Einfach</small>20.50<small>Garniert</small></span></div>
          <div class="item"><div class="item-line"><span class="item-name">THONSALAT</span><span class="leader"></span><span class="price">21.50</span></div><p class="item-desc">garniert mit Rüebli, Oliven, Mais &amp; Zwiebeln</p></div>
          <div class="item"><div class="item-line"><span class="item-name">FITNESSTELLER</span><span class="leader"></span><span class="price">25.50</span></div><p class="item-desc">mit Pouletstreifen</p></div>
          <div class="item"><div class="item-line"><span class="item-name">SALAT «SEEBLICK»</span><span class="leader"></span><span class="price">27.50</span></div><p class="item-desc">Eisberg Salat, Speckstreifen, Croutons, Parmigiano DOP &amp; Pouletstreifen an französische Sauce</p></div>
        </div>
      </div>
      <div class="photo" role="img" aria-label="Foto Salat mit Pouletstreifen" style="width:188px;height:80px;margin:22px auto 0;background:linear-gradient(135deg,#7a9a3a,#d9a050,#a0b860,#5a7a2a)"></div>
      <p class="sheet-footer">Alle Preise verstehen sich in CHF und inkl. Mehrwertsteuer.</p>
    </div>
  </div>

  <div class="page">
    <div class="page-bg bg-food" role="img" aria-label="Foto unscharfe Speisen"></div>
    <div class="sheet">
      <h2 class="section-title" style="margin-top:6px">VORSPEISE</h2>
      <div class="narrow" style="margin-top:4px">
        <div class="item split"><div class="split-main"><div class="item-line"><span class="item-name">BEEFSTEAK TATAR</span><span class="leader"></span></div><p class="item-desc">aus Schweizer Qualitätsrindfleisch, abgeschmeckt nach Ihrem Wunsch, serviert mit Toastbrot &amp; Butter</p></div><span class="price-block">19.50<small>Vorspeise</small>30.50<small>Hauptgang</small></span></div>
        <div class="item"><div class="item-line"><span class="item-name">TOMATEN BRUSCHETTA</span><span class="leader"></span><span class="price">11.50</span></div><p class="item-desc">Tomaten, Knoblauch, Basilikum, Olivenöl &amp; Balsamico Crema</p></div>
        <div class="item"><div class="item-line"><span class="item-name">HUMMUS</span><span class="leader"></span><span class="price">12.50</span></div><p class="item-desc">Kichererbsen, Tahini (Sesampaste), Knobli, Olivenöl &amp; Gewürze, serviert mit Toastbrot</p></div>
        <div class="item"><div class="item-line"><span class="item-name">BURRATA</span><span class="leader"></span><span class="price">17.00</span></div><p class="item-desc">Mit frischem Pesto, Cherry Tomaten, Ruccola, Olivenöl &amp; Balsamico Crème</p></div>
      </div>
      <div class="photo-row" style="margin-top:28px">
        <div class="photo" role="img" aria-label="Foto Burrata mit Tomaten" style="width:91px;height:80px;background:linear-gradient(135deg,#c8321e,#f2efe8,#7a9a3a)"></div>
        <div class="photo" role="img" aria-label="Foto Tatar mit Toastbrot" style="width:140px;height:80px;background:linear-gradient(135deg,#e8dcc8,#c8502e,#d9b070)"></div>
      </div>
      <h2 class="section-title" style="margin-top:38px">FÜR UNSERE KLEINEN GÄSTE</h2>
      <div class="narrow" style="margin-top:4px">
        <div class="item"><div class="item-line"><span class="item-name">PIZZA BAMBINI</span><span class="leader"></span><span class="price">14.50</span></div><p class="item-desc">Pizza Margherita</p></div>
        <div class="item"><div class="item-line"><span class="item-name">SPAGHETTI BIMBI</span><span class="leader"></span><span class="price">14.50</span></div><p class="item-desc">Spaghetti Napoletana</p></div>
        <div class="item"><div class="item-line"><span class="item-name">KLEINE ENTE</span><span class="leader"></span><span class="price">14.50</span></div><p class="item-desc">Chicken Nuggets mit Tartarsauce &amp; Pommes Frites</p></div>
        <div class="item"><div class="item-line"><span class="item-name">KLEINE MAUS</span><span class="leader"></span><span class="price">16.00</span></div><p class="item-desc">Fischknusperli mit Tartarsauce &amp; Pommes Frites</p></div>
      </div>
      <p class="sheet-footer">Alle Preise verstehen sich in CHF und inkl. Mehrwertsteuer.</p>
    </div>
  </div>
</section>

<!-- Spread 3 -->
<section class="spread spread-3">
  <div class="page">
    <div class="page-bg bg-lake2" role="img" aria-label="Foto See mit Bergen"></div>
    <div class="sheet">
      <h2 class="section-title" style="margin-top:6px">PASTA – TEIGWAREN</h2>
      <div class="cols" style="margin-top:6px;gap:30px">
        <div class="col">
          <div class="item"><div class="item-line"><span class="item-name">SPAGHETTI<br>VEGI</span><span class="leader"></span><span class="price">21.50</span></div><p class="item-desc">mit Knoblauch &amp; verschiedene Gemüse an Olivenöl</p></div>
          <div class="item"><div class="item-line"><span class="item-name">SPAGHETTI<br>ALLA NAPOLETANA</span><span class="leader"></span><span class="price">19.50</span></div><p class="item-desc">mit Tomatensauce &amp; frischem Basilikum</p></div>
          <div class="item"><div class="item-line"><span class="item-name">SPAGHETTI<br>ALLA CARBONARA</span><span class="leader"></span><span class="price">23.50</span></div><p class="item-desc">mit Speck, Parmesan, Rahm und Eigelb</p></div>
          <div class="item"><div class="item-line"><span class="item-name">SPAGHETTI<br>AGLIO E OLIO</span><span class="leader"></span><span class="price">28.50</span></div><p class="item-desc">mit 4 Stück Riesencrevetten</p></div>
        </div>
        <div class="col">
          <div class="item"><div class="item-line"><span class="item-name">PENNE<br>ALL'ARRABBIATA</span><span class="leader"></span><span class="price">20.50</span></div><p class="item-desc">an Tomatensauce, Peperoncini &amp; Knoblauch</p></div>
          <div class="item"><div class="item-line"><span class="item-name">TAGLIATELLE<br>AL SEEDORF</span><span class="leader"></span><span class="price">25.50</span></div><p class="item-desc">mit Pouletstreifen &amp; Peperoncini an einer Champignon-Rahmsauce</p></div>
          <div class="item"><div class="item-line"><span class="item-name">TAGLIATELLE<br>AL TARTUFO</span><span class="leader"></span><span class="price">28.50</span></div><p class="item-desc">mit Rindsfiletstreifen &amp; Trüffelöl an einer Champignon-Rahmsauce</p></div>
        </div>
      </div>
      <div class="photo" role="img" aria-label="Foto Pastateller auf Terrasse mit Weinglas" style="width:188px;height:80px;margin:26px auto 0;background:linear-gradient(135deg,#3a4a5a,#e0a050,#f2efe8,#7a2a2a)"></div>
      <h2 class="section-title" style="margin-top:44px">UNSERE FISCHPARADE</h2>
      <div class="narrow" style="margin-top:4px;width:175px">
        <div class="item"><div class="item-line"><span class="item-name">RIESENCREVETTEN<br>NACH„ART DES HAUSES"</span><span class="leader"></span><span class="price">39.50</span></div><p class="item-desc">mit Kräuterbutter, serviert mit Reis und Gemüse</p></div>
        <div class="item"><div class="item-line"><span class="item-name">ZANDERFILET VOM GRILL</span><span class="leader"></span><span class="price">34.50</span></div><p class="item-desc">mit Kräuterbutter, dazu Spinat und Salzkartoffeln</p></div>
        <div class="item"><div class="item-line"><span class="item-name">EGLI-FISCHKNUSPERLI</span><span class="leader"></span><span class="price">29.50</span></div><p class="item-desc">mit Tartarsauce &amp; Pommes frites</p></div>
      </div>
      <p class="sheet-footer">Alle Preise verstehen sich in CHF und inkl. Mehrwertsteuer.</p>
    </div>
  </div>

  <div class="page">
    <div class="page-bg bg-tomato" role="img" aria-label="Foto Tomaten und Gemüse unscharf"></div>
    <div class="sheet">
      <h2 class="section-title" style="margin-top:6px">HAUPTGERICHTE</h2>
      <div class="narrow" style="margin-top:4px">
        <div class="item"><div class="item-line"><span class="item-name">GYROSTELLER MIT<br>SCHWEINEHALSFLEISCH</span><span class="leader"></span><span class="price">30.50</span></div><p class="item-desc">serviert mit Salatbouquet, Tzatziki &amp; Pommes Frites</p></div>
        <div class="item"><div class="item-line"><span class="item-name">SCHWEINS CORDON BLEU</span><span class="leader"></span><span class="price">32.50</span></div><p class="item-desc">gefüllt mit würzigem Vorderschinken, Gruyère, Taleggio DOP &amp; Raclett-Käse, serviert mit Gemüse und Pommes</p></div>
        <div class="item"><div class="item-line"><span class="item-name">WIENER SCHNITZEL VOM KALB</span><span class="leader"></span><span class="price">35.50</span></div><p class="item-desc">mit Pommes frites und Preiselbeeren</p></div>
        <div class="item"><div class="item-line"><span class="item-name">CHICKEN-FINGERS</span><span class="leader"></span><span class="price">26.50</span></div><p class="item-desc">Hausgemachte würzige panierte Pouletstreifen, dazu Sweet-Chili Sauce und Pommes frites</p></div>
      </div>
      <div class="photo-row" style="margin-top:30px">
        <div class="photo" role="img" aria-label="Foto Chicken-Fingers mit Pommes" style="width:91px;height:80px;background:linear-gradient(135deg,#f2efe8,#e0a040,#c8502e)"></div>
        <div class="photo" role="img" aria-label="Foto Steak mit Ofenkartoffel" style="width:140px;height:80px;background:linear-gradient(135deg,#8a5a3a,#d9b070,#5a3a2a,#c89050)"></div>
      </div>
      <h2 class="section-title" style="margin-top:26px">UNSERE GRILLEMPFEHLUNGEN<br>AUF DEM HEISSEN STEIN</h2>
      <div class="narrow" style="margin-top:4px">
        <div class="item"><div class="item-line"><span class="item-name">POULETBRUST</span><span class="leader"></span><span class="price">30.50</span></div><p class="item-desc">200 g</p></div>
        <div class="item"><div class="item-line"><span class="item-name">SCHWEINESTEAK</span><span class="leader"></span><span class="price">32.50</span></div><p class="item-desc">200 g</p></div>
        <div class="item"><div class="item-line"><span class="item-name">RINDSFILET</span><span class="leader"></span><span class="price">35.50</span></div><p class="item-desc">200 g</p></div>
      </div>
      <div class="extras">
        <div><h4>SAUCE NACH WAHL</h4>PFEFFERRAHMSAUCE<br>CHAMPIGNONRAHMSAUCE<br>KRÄUTERBUTTER</div>
        <div><h4>BEILAGE NACH WAHL</h4>POMMES FRITES<br>RÖSTIKROKETTEN<br>GRILLGEMÜSE<br>REIS</div>
      </div>
      <p class="sheet-footer">Alle Preise verstehen sich in CHF und inkl. Mehrwertsteuer.</p>
    </div>
  </div>
</section>

</body>
</html>
```